Leaflet to promote a new sports massage business

I am a Remedial and Sports Massage therapist and treat a range of people from professionals who spend hours working behind computers and have associated neck and back pain through poor posture to amateur sports people of varying intensity/ability - who encounter injuries along the way, or just need some good old stretching out.Remedial and sports massage helps people who have musculoskeletal injury, pain or dysfunction brought about by the stresses and strains of life. Through massage i can reduce pain, promote recovery after injury, relieve stress, and improve flexibility. All of this contributes to helping people feel better. I have just started working at a new location (address attached) and am looking to raise awareness that I am there and to promote the benefits of massage to encourage new clients(attached as a separate document). I have a business card (attached to the brief) which uses hands as the main device, I would like to include these – possibly in some sort of logo and I would like to use purple as a key colour (if colour is used). I also want to include the KVTB logo (attached) to add credibility

```html
<!DOCTYPE html>
<html lang="en">
<head>
<meta charset="utf-8">
<title>Harriet Linwood – Remedial and Sports Massage Therapist</title>
<link rel="stylesheet" href="https://fonts.googleapis.com/css2?family=Questrial&display=swap">
<style>
  :root {
    --plum: #5a1752;
    --plum-bar: #6c2a66;
    --plum-hands: #5e1a5a;
    --plum-hands-light: #7a3574;
    --blush: #f3cbe3;
    --veil: rgba(240, 222, 214, 0.8);
    --circle-fill: rgba(236, 218, 214, 0.9);
    --skin: #e4b8a0;
    --sport-blue: #3f8fd6;
    --towel-grey: #7d8a99;
    --towel-white: #eef0f2;
    --room: #ece0d8;
  }
  * { margin: 0; padding: 0; box-sizing: border-box; }
  html, body { width: 1200px; height: 850px; overflow: hidden; background: #fff; }
  body { font-family: "Questrial", sans-serif; color: var(--plum); }

  .leaflet { position: relative; width: 1200px; height: 850px; overflow: hidden; }

  .hero-photo {
    position: absolute; inset: 0;
    background:
      radial-gradient(ellipse 300px 140px at 350px 560px, var(--skin) 0%, rgba(228,184,160,0.85) 55%, rgba(228,184,160,0) 100%),
      radial-gradient(ellipse 240px 110px at 860px 240px, var(--skin) 0%, rgba(228,184,160,0) 100%),
      radial-gradient(ellipse 520px 190px at 820px 420px, var(--sport-blue) 0%, rgba(63,143,214,0.9) 45%, rgba(63,143,214,0) 100%),
      radial-gradient(ellipse 260px 80px at 370px 680px, var(--towel-white) 0%, rgba(238,240,242,0) 100%),
      linear-gradient(180deg, var(--room) 0%, #e6d2c6 30%, #d9c3b8 48%, #a9aeb6 66%, var(--towel-grey) 80%, #6f7a88 100%);
  }

  .title-veil { position: absolute; left: 0; top: 0; width: 1200px; height: 240px; }

  .masthead { position: absolute; left: 0; top: 42px; width: 772px; text-align: center; }
  .masthead__name { font-size: 47px; font-weight: 400; letter-spacing: 0.5px; line-height: 1; -webkit-text-stroke: 0.6px var(--plum); }
  .masthead__role { font-size: 34px; font-weight: 400; margin-top: 12px; line-height: 1; -webkit-text-stroke: 0.3px var(--plum); }

  .benefits {
    position: absolute; left: 648px; top: 270px; width: 300px; height: 300px;
    border-radius: 50%; background: var(--circle-fill);
    border: 2px dotted var(--plum);
    display: flex; flex-direction: column; align-items: center; justify-content: center;
    text-align: center; padding-bottom: 12px;
  }
  .benefits__heading { font-size: 38px; font-weight: 400; line-height: 1; -webkit-text-stroke: 0.4px var(--plum); }
  .benefits__of { font-size: 19px; line-height: 1; margin: 2px 0 6px; }
  .benefits__list { list-style: none; margin-top: 8px; font-size: 16.5px; line-height: 19.5px; }

  .hands-motif { position: absolute; left: 930px; top: 508px; width: 270px; height: 242px; }

  .accreditation {
    position: absolute; left: 60px; top: 760px;
    display: flex; align-items: center; gap: 8px;
  }
  .accreditation__dot { width: 18px; height: 18px; border-radius: 50%; background: var(--plum); }
  .accreditation__name { font-size: 22px; color: var(--plum); letter-spacing: 2px; }

  .contact-bar {
    position: absolute; left: 162px; top: 749px; width: 944px; height: 110px;
    background: var(--plum-bar); border-radius: 24px 24px 0 0;
    color: var(--blush); font-size: 18px;
  }
  .contact-item { position: absolute; display: flex; align-items: center; gap: 9px; white-space: nowrap; }
  .contact-item svg { flex: none; }
  .contact-item--address { left: 92px; top: 12px; gap: 12px; }
  .contact-item--phone { left: 92px; top: 51px; }
  .contact-item--web { left: 248px; top: 51px; }
  .contact-item--email { left: 620px; top: 51px; }
</style>
</head>
<body>
<main class="leaflet">
  <div class="hero-photo" role="img" aria-label="Photograph of a therapist massaging the shoulder of a woman in a blue sports top lying on her side on a towel-covered treatment table"></div>

  <svg class="title-veil" viewBox="0 0 1200 240" aria-hidden="true">
    <path d="M0 0 H1200 V132 C900 150 560 250 320 224 C190 212 80 196 0 184 Z" fill="var(--veil)"/>
  </svg>

  <header class="masthead">
    <h1 class="masthead__name">HARRIET LINWOOD</h1>
    <p class="masthead__role">Remedial and Sports Massage Therapist</p>
  </header>

  <section class="benefits">
    <h2 class="benefits__heading">BENEFITS</h2>
    <span class="benefits__of">of</span>
    <h2 class="benefits__heading">MASSAGE</h2>
    <ul class="benefits__list">
      <li>Reduces pain</li>
      <li>Promotes recovery</li>
      <li>Improves posture and flexibility</li>
      <li>Relieves stress</li>
      <li>Improves health and wellbeing</li>
    </ul>
  </section>

  <div class="hands-motif" role="img" aria-label="Illustration of two overlapping purple hands, the business's hand device">
    <svg viewBox="0 0 270 242" width="270" height="242" aria-hidden="true">
      <defs>
        <radialGradient id="handsTone" cx="0.7" cy="0.35" r="0.8">
          <stop offset="0" stop-color="var(--plum-hands-light)"/>
          <stop offset="1" stop-color="var(--plum-hands)"/>
        </radialGradient>
      </defs>
      <path d="M0 242 C40 200 70 150 95 110 C120 60 170 15 230 5 C250 2 262 4 270 8 V242 Z" fill="url(#handsTone)"/>
    </svg>
  </div>

  <div class="accreditation">
    <span class="accreditation__dot"></span>
    <span class="accreditation__name">KVTB</span>
  </div>

  <footer class="contact-bar">
    <span class="contact-item contact-item--address">
      <svg width="14" height="20" viewBox="0 0 14 20" aria-hidden="true"><path d="M7 0a7 7 0 0 0-7 7c0 5 7 13 7 13s7-8 7-13a7 7 0 0 0-7-7zm0 10a3 3 0 1 1 0-6 3 3 0 0 1 0 6z" fill="var(--blush)"/></svg>
      Stride Physio Clinic - Hollybrook Sports Ground - Ashdown Lane - Westbury - WB4 7QD
    </span>
    <span class="contact-item contact-item--phone">
      <svg width="16" height="16" viewBox="0 0 16 16" aria-hidden="true"><rect x="0" y="0" width="16" height="16" rx="3" fill="var(--blush)"/><path d="M5 3.5l2 2-1.2 1.3c.6 1.3 1.7 2.3 2.9 2.9L10 8.5l2 2-1.3 1.7C7 12 4 9 3.8 5.3z" fill="var(--plum-bar)"/></svg>
      07700 900418
    </span>
    <span class="contact-item contact-item--web">
      <svg width="18" height="18" viewBox="0 0 18 18" aria-hidden="true" fill="none" stroke="var(--blush)" stroke-width="1.3"><circle cx="9" cy="9" r="8"/><ellipse cx="9" cy="9" rx="3.5" ry="8"/><path d="M1 9h16M2.5 5h13M2.5 13h13"/></svg>
      www.harrietlinwoodsportsmassage.com
    </span>
    <span class="contact-item contact-item--email">
      <svg width="30" height="18" viewBox="0 0 30 18" aria-hidden="true" fill="none" stroke="var(--blush)" stroke-width="1.5"><rect x="1" y="1" width="28" height="16"/><path d="M1 1l14 10L29 1M1 17l10-8M29 17l-10-8"/></svg>
      harrietlinwood@mailbox.com
    </span>
  </footer>
</main>
</body>
</html>
```